Financial Services Business Card Design

We are a financial services company Based in London, offering Short term Funding Solutions for companies, raising anywhere between £20,000 and £25million pounds.

The Card must have a professional look as it is going to be handed out to professionals I.E Solicitors, Accountants, Company directors and Business owners.

See Attached our company Logo

Industry/Entity Type

Business

Contact Information for Business Card

Lewis Thorncroft
Suite 41
R K House
Bramblecote Lane
Watford
HP19 4QX

```html
<!DOCTYPE html>
<html lang="en">
<head>
<meta charset="utf-8">
<title>Kestrel Funding Centre – Business Card</title>
<link href="https://fonts.googleapis.com/css2?family=Source+Sans+3:wght@400;600;700&display=swap" rel="stylesheet">
<style>
  :root {
    --stage-top: #2a2a2a;
    --stage-bottom: #050505;
    --card-light: #f3f3f3;
    --brand-green: #39a935;
    --brand-green-deep: #31992f;
    --brand-blue: #1f6db5;
    --ink: #1e1e1e;
    --white: #ffffff;
  }
  * { margin: 0; padding: 0; box-sizing: border-box; }
  html, body { width: 1200px; height: 900px; overflow: hidden; }
  body {
    background: linear-gradient(180deg, var(--stage-top) 0%, var(--stage-bottom) 100%);
    font-family: "Source Sans 3", "Myriad Pro", Arial, sans-serif;
    position: relative;
  }
  .card {
    position: absolute;
    top: 184px;
    width: 302px;
    height: 490px;
    border-radius: 13px;
    overflow: hidden;
  }
  .card--front { left: 299px; background: var(--card-light); color: var(--ink); text-align: center; }
  .card--back {
    left: 645px;
    width: 304px;
    background: linear-gradient(160deg, var(--brand-green) 0%, var(--brand-green-deep) 100%);
  }
  .brand-mark {
    position: absolute;
    left: 131px; top: 60px;
    width: 40px; height: 40px;
    border-radius: 50%;
    background: var(--brand-green);
  }
  .brand-name {
    position: absolute;
    left: 0; right: 0;
    top: 116px;
    padding: 0 20px;
    font-weight: 700;
    font-size: 26px;
    line-height: 29px;
    letter-spacing: 0.5px;
    text-transform: uppercase;
    color: var(--brand-blue);
  }
  .holder-name {
    position: absolute;
    left: 0; right: 0; top: 284px;
    font-size: 19px;
    font-weight: 600;
    color: var(--brand-green);
  }
  .contact-list {
    position: absolute;
    left: 0; right: 0; top: 343px;
    list-style: none;
    font-size: 14.5px;
    line-height: 20px;
  }
  .contact-list li { display: flex; justify-content: center; align-items: center; gap: 5px; }
  .contact-list svg { width: 10px; height: 10px; fill: var(--brand-green); }
  .address {
    position: absolute;
    left: 0; right: 0; top: 427px;
    font-style: normal;
    font-size: 14.5px;
    line-height: 20px;
  }
  .back-name {
    position: absolute;
    left: 0; right: 0; top: 398px;
    text-align: center;
    font-weight: 700;
    font-size: 30px;
    line-height: 32px;
    letter-spacing: 0.5px;
    text-transform: uppercase;
    color: var(--white);
  }
</style>
</head>
<body>
  <section class="card card--front" aria-label="Business card front">
    <span class="brand-mark" aria-hidden="true"></span>
    <div class="brand-name">Kestrel<br>Funding Centre</div>
    <div class="holder-name">Lewis Thorncroft</div>
    <ul class="contact-list">
      <li>
        <svg viewBox="0 0 10 10" aria-hidden="true"><path d="M2 0.5 L3.6 2.6 L2.7 3.6 Q4 6 6.4 7.3 L7.4 6.4 L9.5 8 L8.3 9.5 Q4.5 9.2 2.2 6.5 Q0.4 4.2 0.5 1.6 Z"/></svg>
        (044)-555-0142
      </li>
      <li>
        <svg viewBox="0 0 10 10" aria-hidden="true"><rect x="0" y="1.5" width="10" height="7"/><path d="M0 1.8 L5 5.5 L10 1.8" fill="none" stroke="#f3f3f3" stroke-width="1"/></svg>
        info@kestrelfunding.com
      </li>
      <li>
        <svg viewBox="0 0 10 10" aria-hidden="true"><circle cx="5" cy="5" r="5"/><path d="M2.5 3 Q4 2 5 3.5 Q4 5 5.5 6.5 L4.5 8.5 M6.5 1.5 L7.5 3 L8.8 3.2" fill="none" stroke="#f3f3f3" stroke-width="0.9"/></svg>
        www.kestrelfunding.co.uk
      </li>
    </ul>
    <address class="address">Suite 41, R K House Bramblecote<br>Lane, Watford, HP19 4QX</address>
  </section>

  <section class="card card--back" aria-label="Business card back">
    <div class="back-name">Kestrel<br>Funding Centre</div>
  </section>
</body>
</html>
```